Kelvo Tech Oz Business card revamp

We are looking to revamp our business card design. We are hoping to change our colours to dark navey blue, gray, white and black but are open to keeping the same if a good design is submited. We are after somthing a bit differnt not just boring business card. I have attached a copy of our current card. We Want to keep the same logo design which i have attached a few to hopfully help you in this process. We are after a design that can be personalized to separate 4 people

Colors
0455a3
ffffff
000000
cbcbcb

Requirements
Must have
• Kelvo Tech Logo, address 3/41 Mallory Court, Wexhill 4218, phone number, Name and position

```html
<!DOCTYPE html>
<html lang="en">
<head>
<meta charset="utf-8">
<title>Kelvo Tech Oz – Business Card</title>
<link rel="stylesheet" href="https://fonts.googleapis.com/css2?family=Josefin+Sans:wght@400;600&family=Poppins:wght@500;700;800&display=swap">
<style>
  :root {
    --brand-blue: #0455a3;
    --brand-orange: #f07a22;
    --ink: #000000;
    --paper: #ffffff;
    --grey: #cbcbcb;
    --backdrop: #ecebe8;
    --icon-cyan: #2a9fd6;
  }
  * { box-sizing: border-box; margin: 0; padding: 0; }
  html, body {
    width: 1200px; height: 1000px; overflow: hidden;
    background: var(--backdrop);
  }
  .sheet {
    width: 1200px; height: 1000px;
    display: flex; flex-direction: column;
    align-items: center; justify-content: center; gap: 40px;
  }
  .card {
    position: relative;
    width: 760px; height: 434px;
    overflow: hidden;
    box-shadow: 0 6px 18px rgba(0,0,0,.18);
  }
  /* Back */
  .card--back {
    background: var(--ink);
    display: flex; align-items: center; justify-content: center;
  }
  .brand {
    display: flex; align-items: center; gap: 14px;
    font-family: "Poppins", sans-serif; font-weight: 800;
  }
  .brand__dot { border-radius: 50%; flex: none; }
  .card--back .brand__name { color: var(--paper); font-size: 64px; letter-spacing: -1px; }
  .card--back .brand__dot { width: 46px; height: 46px; background: var(--paper); }
  /* Front */
  .card--front { background: var(--paper); }
  .card--front .brand {
    position: absolute; top: 44px; right: 42px; gap: 10px;
  }
  .card--front .brand__name { color: var(--brand-blue); font-size: 34px; letter-spacing: -.5px; }
  .card--front .brand__dot { width: 26px; height: 26px; background: var(--brand-orange); }
  .person { position: absolute; left: 46px; top: 150px; }
  .person__name {
    font-family: "Josefin Sans", sans-serif; font-weight: 400;
    font-size: 34px; letter-spacing: 3px; color: var(--ink);
  }
  .person__role {
    font-family: "Josefin Sans", sans-serif; font-weight: 600;
    font-size: 16px; letter-spacing: 1.5px; color: var(--brand-blue);
    margin-top: 4px;
  }
  .contact {
    position: absolute; left: 46px; top: 285px;
    list-style: none; display: flex; flex-direction: column; gap: 20px;
    font-family: "Poppins", sans-serif; font-weight: 500;
    font-size: 17px; color: var(--ink);
  }
  .contact__item { display: flex; align-items: center; gap: 14px; }
  .contact__icon { width: 14px; height: 14px; flex: none; }
  .band { position: absolute; bottom: 0; }
  .band--black { left: 0; width: 71%; height: 40px; background: var(--ink); }
  .band--blue { right: 0; width: 28%; height: 66px; background: var(--brand-blue); }
</style>
</head>
<body>
<main class="sheet">
  <section class="card card--back" aria-label="Card back">
    <div class="brand">
      <span class="brand__dot"></span>
      <span class="brand__name">Kelvo Tech</span>
    </div>
  </section>

  <section class="card card--front" aria-label="Card front">
    <div class="brand">
      <span class="brand__dot"></span>
      <span class="brand__name">Kelvo Tech</span>
    </div>

    <div class="person">
      <h1 class="person__name">JOHN DOE</h1>
      <p class="person__role">GENERAL MANAGER</p>
    </div>

    <ul class="contact">
      <li class="contact__item">
        <svg class="contact__icon" viewBox="0 0 24 24" aria-hidden="true">
          <path fill="var(--icon-cyan)" d="M6.6 10.8a15.1 15.1 0 0 0 6.6 6.6l2.2-2.2a1 1 0 0 1 1-.25 11.4 11.4 0 0 0 3.6.6 1 1 0 0 1 1 1V20a1 1 0 0 1-1 1A17 17 0 0 1 3 4a1 1 0 0 1 1-1h3.5a1 1 0 0 1 1 1c0 1.25.2 2.45.6 3.6a1 1 0 0 1-.25 1z"/>
        </svg>
        <span>+123 456 789 101</span>
      </li>
      <li class="contact__item">
        <svg class="contact__icon" viewBox="0 0 24 24" aria-hidden="true">
          <path fill="var(--icon-cyan)" d="M12 2a7 7 0 0 0-7 7c0 5.2 7 13 7 13s7-7.8 7-13a7 7 0 0 0-7-7zm0 9.5A2.5 2.5 0 1 1 12 6.5a2.5 2.5 0 0 1 0 5z"/>
        </svg>
        <span>3/41 Mallory Court, Wexhill 4218</span>
      </li>
    </ul>

    <div class="band band--black"></div>
    <div class="band band--blue"></div>
  </section>
</main>
</body>
</html>
```